Lotus Leaf Kitchen Road Billboard

Road Billboard I need all of this information on it
Authentic Thai Food Bangkok Style
6.5 Miles on the right
4126 Maple Ridge Rd Otto NC
828-555-4172

```html
<!DOCTYPE html>
<html lang="en">
<head>
<meta charset="UTF-8">
<title>Lotus Leaf Kitchen Road Billboard</title>
<link href="https://fonts.googleapis.com/css2?family=Montserrat:wght@600;700;800&display=swap" rel="stylesheet">
<style>
  :root {
    --page: #eef1f4;
    --board: #050505;
    --gold: #d6a915;
    --ink: #0a0a0a;
    --white: #ffffff;
    --flame: #e0661a;
    --ember: #3a1a08;
  }
  * { margin: 0; padding: 0; box-sizing: border-box; }
  html, body { width: 1200px; height: 1155px; overflow: hidden; background: var(--page); }
  .billboard {
    position: absolute; left: 20px; top: 347px;
    width: 1160px; height: 460px;
    background: var(--board); overflow: hidden;
    font-family: "Montserrat", sans-serif;
  }
  .direction-band { position: absolute; left: 30px; top: 22px; width: 680px; height: 66px; }
  .direction-text {
    position: absolute; left: 80px; top: 30px; height: 50px; line-height: 50px;
    font-weight: 800; font-size: 42px; color: var(--ink); letter-spacing: 0.5px;
  }
  .dish-photo {
    position: absolute; left: 690px; top: 88px; width: 470px; height: 312px;
    background: radial-gradient(ellipse at 40% 45%, var(--flame) 0%, var(--ember) 45%, var(--board) 80%);
  }
  .brand {
    position: absolute; left: 130px; top: 114px; width: 480px; text-align: center;
  }
  .brand-mark {
    width: 80px; height: 80px; border-radius: 50%; background: var(--gold);
    margin: 0 auto 16px;
  }
  .brand-name { font-weight: 700; font-size: 44px; line-height: 54px; color: var(--gold); white-space: nowrap; }
  .tagline {
    margin-top: 10px; font-weight: 600; font-size: 20px; line-height: 26px;
    color: var(--white); white-space: nowrap; letter-spacing: 0.5px;
  }
  .phone-band { position: absolute; left: 0; top: 338px; width: 760px; height: 122px; }
  .phone {
    position: absolute; left: 34px; top: 352px; height: 96px;
    display: flex; align-items: center; gap: 26px;
    font-weight: 800; font-size: 84px; color: var(--ink); letter-spacing: 1px;
    white-space: nowrap;
  }
  .address {
    position: absolute; left: 775px; right: 16px; top: 404px; height: 50px;
    display: flex; align-items: center; justify-content: flex-end; gap: 10px;
    font-weight: 600; font-size: 20px; color: var(--white); white-space: nowrap;
  }
</style>
</head>
<body>
  <main class="billboard">
    <svg class="direction-band" viewBox="0 0 680 66" aria-hidden="true">
      <polygon points="0,33 40,0 680,0 680,66 40,66" fill="var(--gold)"/>
    </svg>
    <div class="direction-text">6.5 MILES ON THE RIGHT</div>

    <div class="dish-photo" role="img" aria-label="Stir-fry of shrimp and vegetables tossed over a flaming wok"></div>

    <div class="brand">
      <div class="brand-mark"></div>
      <div class="brand-name">Lotus Leaf Kitchen</div>
      <div class="tagline">Authentic Thai Food Bangkok Style</div>
    </div>

    <svg class="phone-band" viewBox="0 0 760 122" aria-hidden="true">
      <polygon points="0,0 690,0 760,122 0,122" fill="var(--gold)"/>
    </svg>
    <div class="phone">
      <svg width="64" height="64" viewBox="0 0 24 24" aria-hidden="true">
        <path fill="var(--ink)" d="M6.6 10.8a15.1 15.1 0 0 0 6.6 6.6l2.2-2.2a1 1 0 0 1 1-.25 11.4 11.4 0 0 0 3.6.57 1 1 0 0 1 1 1V20a1 1 0 0 1-1 1A17 17 0 0 1 3 4a1 1 0 0 1 1-1h3.5a1 1 0 0 1 1 1c0 1.25.2 2.45.57 3.57a1 1 0 0 1-.25 1z"/>
        <path fill="none" stroke="var(--ink)" stroke-width="1.8" stroke-linecap="round" d="M14.5 3.5a6.5 6.5 0 0 1 6 6M14 7a3 3 0 0 1 3 3"/>
      </svg>
      <span>828-555-4172</span>
    </div>

    <div class="address">
      <svg width="24" height="32" viewBox="0 0 24 32" aria-hidden="true">
        <path fill="var(--gold)" d="M12 0a10 10 0 0 0-10 10c0 7.5 10 18 10 18s10-10.5 10-18A10 10 0 0 0 12 0zm0 14a4 4 0 1 1 0-8 4 4 0 0 1 0 8z"/>
        <ellipse cx="12" cy="30" rx="9" ry="2" fill="var(--gold)"/>
      </svg>
      <span>4126 Maple Ridge Rd Otto NC</span>
    </div>
  </main>
</body>
</html>
```